HARBOR VALE Insurance Business Card Design

We need a business card designed for our personal risk / life insurance business based in Sydney Australia called 'Harbor Vale'.

We manage and implement life insurance policies for individuals, businesses and families. Work on estate planning and succession planning. We help individuals make sure that they will be covered financially in the event of disability or critical illness.

We would like to see designs that use the colours Black, Silver/Grey , White OR different shades of Blue that are suitable for the finance / professional industries.

The final design should communicate financial safety and can also feel contemporary.

Hello,

Thanks for submitting your design.
We have recieved MANY great new designs today, thank-you.
Sorry for the late notice but for legal reasons we must include additional information of the card as follows:

Level 5, Suite 5.31,
47 Wattlebark Lane
MORWENTON NSW 2098

Authorised Representative No. 493172
Tallowmere Wealth Partners Pty Ltd
ABN 47 218 664 905
AFS Licence No. 582904

PLEASE REMOVE:
S marcuspellworth

PLEASE ADD:
www.harborvale-example.com.au

Industry/Entity Type

Life Insurance

Contact Information for Business Card

Marcus Pellworth
Senior Advisor
Managing Director

M +61400 587 294
E Marcus@harborvale-example.com.au
S marcuspellworth

Level 5, Suite 5.31
47 Wattlebark Lane
MORWENTON NSW 2098

Font styles to use
Serif
Sans Serif

Requirements
Must have
• - LANDSCAPE design

- MUST BE DOUBLE SIDED

Level 5, Suite 5.31,
47 Wattlebark Lane
MORWENTON NSW 2098

ABN 47 218 664 905
AFS Licence No. 582904

PLEASE REMOVE:
S marcuspellworth

PLEASE ADD:
www.harborvale-example.com.au
Nice to have
• - Can have a rounded corner... but doesn't have to

```html
<!DOCTYPE html>
<html lang="en">
<head>
<meta charset="UTF-8">
<title>Harbor Vale – Business Card</title>
<link rel="stylesheet" href="https://fonts.googleapis.com/css2?family=Open+Sans:wght@400;600&display=swap">
<style>
  :root {
    --stage: #1e1e1f;
    --card: #0f0f10;
    --card-edge: #262628;
    --band-light: #5f6566;
    --band-mid: #454a4b;
    --band-dark: #2f3334;
    --rule: #4a4f50;
    --text-main: #f2f2f2;
    --text-soft: #c9cbcc;
    --text-label: #9a9d9e;
  }
  * { margin: 0; padding: 0; box-sizing: border-box; }
  html, body {
    width: 1200px;
    height: 1000px;
    overflow: hidden;
    background: var(--stage);
    font-family: "Open Sans", Arial, sans-serif;
  }
  .stage {
    position: relative;
    width: 1200px;
    height: 1000px;
  }
  .card {
    position: absolute;
    left: 220px;
    width: 760px;
    height: 422px;
    background: var(--card);
    border: 1px solid var(--card-edge);
    overflow: hidden;
  }
  .card--front { top: 52px; }
  .card--back { top: 526px; }

  /* brand name */
  .brand {
    display: flex;
    align-items: center;
    gap: 12px;
    color: var(--text-main);
    font-weight: 600;
    letter-spacing: 1px;
  }
  .brand__square {
    width: 40px;
    height: 40px;
    background: var(--band-light);
  }

  /* front side */
  .card--front .brand {
    position: absolute;
    left: 52px;
    top: 92px;
    font-size: 34px;
  }
  .front-bars {
    position: absolute;
    left: 30px;
    top: 236px;
    height: 88px;
    display: flex;
  }
  .front-bars__light { width: 30px; background: var(--band-light); }
  .front-bars__dark { width: 28px; background: var(--band-dark); }
  .holder {
    position: absolute;
    left: 112px;
    top: 246px;
    color: var(--text-main);
  }
  .holder__name { font-size: 29px; font-weight: 400; line-height: 1.15; }
  .holder__role { font-size: 14px; color: var(--text-soft); margin-top: 4px; }

  .contact {
    position: absolute;
    right: 34px;
    top: 40px;
    text-align: right;
    font-size: 12.5px;
    line-height: 1.45;
    color: var(--text-soft);
  }
  .contact__group { margin-bottom: 26px; }
  .contact__label {
    color: var(--text-label);
    text-transform: uppercase;
    font-size: 12px;
  }

  .legal {
    position: absolute;
    left: 30px;
    right: 34px;
    bottom: 22px;
    font-size: 11px;
    line-height: 1.5;
    color: var(--text-label);
  }

  /* back side */
  .back-rule {
    position: absolute;
    left: 0;
    right: 0;
    top: 112px;
    height: 6px;
    background: var(--rule);
  }
  .back-rule--thin { top: 124px; height: 2px; background: var(--band-dark); }
  .back-logo-box {
    position: absolute;
    left: 380px;
    right: 34px;
    top: 136px;
    height: 84px;
    background: #1b1c1d;
    display: flex;
    align-items: center;
    padding-left: 26px;
  }
  .back-logo-box .brand { font-size: 34px; }
  .back-band {
    position: absolute;
    left: 0;
    top: 220px;
    width: 380px;
    height: 96px;
    display: flex;
  }
  .back-band__edge { width: 44px; background: var(--band-dark); }
  .back-band__fill { flex: 1; background: var(--band-light); }
  .back-web {
    position: absolute;
    left: 380px;
    right: 34px;
    top: 280px;
    text-align: center;
    color: var(--text-soft);
    font-size: 13px;
    letter-spacing: 1px;
  }
</style>
</head>
<body>
<main class="stage">

  <section class="card card--front" aria-label="Business card front">
    <div class="brand">
      <span class="brand__square"></span>
      <span class="brand__name">HARBOR VALE</span>
    </div>

    <div class="front-bars">
      <span class="front-bars__light"></span>
      <span class="front-bars__dark"></span>
    </div>

    <div class="holder">
      <p class="holder__name">Marcus Pellworth</p>
      <p class="holder__role">Senior Advisor Managing Director</p>
    </div>

    <div class="contact">
      <div class="contact__group">
        <p class="contact__label">Address</p>
        <p>Level 5, Suite 5.31</p>
        <p>47 Wattlebark Lane MORWENTON NSW 2098</p>
      </div>
      <div class="contact__group">
        <p class="contact__label">Phone</p>
        <p>+61400 587 294</p>
      </div>
      <div class="contact__group">
        <p class="contact__label">Web</p>
        <p>Marcus@harborvale-example.com.au</p>
        <p>www.harborvale-example.com.au</p>
      </div>
    </div>

    <div class="legal">
      <p>Authorised Representative No. 493172 of Tallowmere Wealth Partners Pty Ltd</p>
      <p>ABN 47 218 664 905 &nbsp;·&nbsp; AFS Licence No. 582904</p>
    </div>
  </section>

  <section class="card card--back" aria-label="Business card back">
    <span class="back-rule"></span>
    <span class="back-rule back-rule--thin"></span>

    <div class="back-logo-box">
      <div class="brand">
        <span class="brand__square"></span>
        <span class="brand__name">HARBOR VALE</span>
      </div>
    </div>

    <div class="back-band">
      <span class="back-band__edge"></span>
      <span class="back-band__fill"></span>
    </div>

    <p class="back-web">WWW.HARBORVALE-EXAMPLE.COM.AU</p>
  </section>

</main>
</body>
</html>
```